Hot-air ballooning company needs a DL-size flyer

Skylark Aerial Tours is a hot-air ballooning company which flies passengers in the King Valley, Victoria, Australia.
We need a 2-sided DL-size flyer which promotes our hot-air balloon flights and packages.
Most of our customers are couples, and we want the flyer design to communicate safety, adventure, and romance.
The flyer should make the best use of our images which we provide, and we've also included a document with the text for the flyer.
Updates

2 days is not long enough to gather designs, the brief never asked me what my deadline should be.

Target Market(s)

Couples, buyers are majority female, between the ages of 20-60

Industry/Entity Type

Tourism

Font styles to use
Sans Serif

Colors

Designer to choose colors to be used in the design.

Requirements
Must have
• Communicate safety, adventure, and romance
• Use images
Nice to have
• There is a lot of text, it would be great if you could make it look like as little text as possible
Should not have
• No childish designs

```html
<!DOCTYPE html>
<html lang="en">
<head>
<meta charset="utf-8">
<title>King Valley Hot-Air Ballooning – Skylark Aerial Tours</title>
<link rel="stylesheet" href="https://fonts.googleapis.com/css2?family=Arimo:wght@400;700&family=Roboto+Condensed:wght@400&family=Questrial&display=swap">
<style>
  :root {
    --page-bg: #e9e6e1;
    --brand-blue: #4170c2;
    --brand-blue-deep: #2f56a8;
    --brand-blue-light: #8fb0e4;
    --sky-top: #3a86d0;
    --sky-mid: #9ccbea;
    --valley-mist: #c9d6df;
    --valley-ground: #6d6a55;
    --text-dark: #1e1e1e;
    --white: #ffffff;
  }
  * { margin: 0; padding: 0; box-sizing: border-box; }
  html, body { width: 1200px; height: 1200px; overflow: hidden; background: var(--page-bg); }
  .stage { position: relative; width: 1200px; height: 1200px; }
  .flyer {
    position: absolute; left: 354px; top: 30px;
    width: 560px; height: 1298px;
    transform: scale(0.8782); transform-origin: top left;
    background: var(--white); overflow: hidden;
    box-shadow: 0 6px 18px rgba(0,0,0,.25);
    font-family: "Roboto Condensed", "Arial Narrow", sans-serif;
    color: var(--text-dark);
  }
  .hero-photo {
    position: absolute; left: 0; top: 0; width: 560px; height: 540px;
    background: linear-gradient(180deg, var(--sky-top) 0%, var(--sky-mid) 48%, var(--valley-mist) 62%, #a9b3b0 78%, var(--valley-ground) 100%);
  }
  .hero-wave { position: absolute; left: 0; top: 420px; width: 560px; height: 140px; }
  .title { position: absolute; right: 30px; text-align: right; font-family: "Arimo", Arial, sans-serif; font-weight: 700; color: var(--white); text-shadow: 2px 2px 4px rgba(0,0,0,.45); }
  .title-main { top: 14px; font-size: 50px; letter-spacing: .5px; }
  .title-sub { top: 72px; font-size: 35px; }
  .inset-photo {
    position: absolute; left: 15px; top: 348px; width: 200px; height: 200px; border-radius: 50%;
    border: 8px solid var(--brand-blue-light);
    background: radial-gradient(circle at 50% 35%, #b9a98e 0%, #7a8a56 45%, #5d5a48 100%);
  }
  .lower-photo {
    position: absolute; left: 0; top: 540px; width: 560px; height: 700px;
    background: linear-gradient(180deg, #f2f6fb 0%, #ffffff 30%, #f4f6f8 55%, #d3d9dc 80%, #c0c7c8 100%);
  }
  .rule { position: absolute; left: 17px; top: 559px; width: 525px; height: 5px; background: var(--brand-blue); }
  .tab {
    position: absolute; left: 102px; top: 559px; width: 356px; height: 90px;
    background: var(--brand-blue); border: 3px solid var(--brand-blue-light); border-top: none;
    border-radius: 0 0 60px 60px;
    font-family: "Questrial", "Century Gothic", sans-serif; color: var(--white);
    font-size: 29px; line-height: 36px; text-align: center; padding-top: 6px;
  }
  .details { position: absolute; left: 20px; top: 656px; width: 520px; text-align: center; font-size: 18.5px; line-height: 23px; }
  .details p { margin-bottom: 4px; }
  .brand { position: absolute; left: 0; top: 985px; width: 560px; display: flex; justify-content: center; align-items: center; gap: 12px; }
  .brand-dot { width: 26px; height: 26px; border-radius: 50%; background: var(--brand-blue); }
  .brand-name { font-size: 30px; color: var(--brand-blue-deep); }
  .contact { position: absolute; left: 0; top: 1105px; width: 560px; text-align: center; }
  .contact-lead { font-size: 16px; }
  .contact-phone { font-family: "Arimo", Arial, sans-serif; font-size: 26px; margin-top: 2px; }
  .contact-line { font-size: 22px; line-height: 28px; }
  .contact-social { font-size: 15px; margin-top: 1px; }
  .licence-band {
    position: absolute; left: 0; top: 1240px; width: 560px; height: 58px;
    background: var(--brand-blue); color: var(--white); text-align: center;
    font-size: 16.5px; line-height: 20px; padding-top: 8px;
    border-top: 3px solid var(--brand-blue-light);
  }
</style>
</head>
<body>
<div class="stage">
  <div class="flyer">
    <div class="hero-photo" role="img" aria-label="Two colourful hot-air balloons flying over misty King Valley vineyards at dawn with mountains behind"></div>
    <svg class="hero-wave" viewBox="0 0 560 140" aria-hidden="true">
      <path d="M200 140 L200 130 C300 200 420 90 560 140 Z" fill="#ffffff"/>
      <path d="M200 118 C260 170 330 190 420 178 C480 170 530 150 560 128 L560 150 C500 180 430 195 360 195 C290 195 240 170 200 140 Z" fill="var(--brand-blue)" transform="translate(0,-30)"/>
      <path d="M230 140 C300 168 400 168 470 150 C510 140 540 128 560 112 L560 122 C520 148 470 162 410 168 C340 172 280 160 230 140 Z" fill="#ffffff" transform="translate(0,-28)"/>
      <path d="M200 140 L560 140 L560 130 C500 150 420 150 330 135 C270 125 230 128 200 140 Z" fill="var(--brand-blue-light)"/>
    </svg>
    <div class="title title-main">KING VALLEY</div>
    <div class="title title-sub">HOT-AIR BALLOONING</div>
    <div class="inset-photo" role="img" aria-label="Passengers in a balloon basket after landing beside a vineyard"></div>

    <div class="lower-photo" role="img" aria-label="Faint misty aerial view of the valley below"></div>
    <div class="rule"></div>
    <div class="tab">The perfect gourmet<br>ballooning experience</div>

    <div class="details">
      <p>Live the romance and adventure of flying the beautiful King Valley and surrounds ina hot-air balloon at dawn</p>
      <p>From the vineyards and patchwork of fields the views expand to the Ovens River, spectacular Mt Buffalo and the High Country beyond</p>
      <p>The mountain views, once aloft, come to life in dramatic 3D with the early morning light</p>
      <p>Celebrate your flight with a delicious breakfast afterwards (optional)</p>
      <p>Milawa is conveniently located less than an hour's drive from most places in Victoria's North East and Albury in NSW</p>
      <p>Mansfield flights are also available</p>
    </div>

    <div class="brand">
      <span class="brand-dot"></span>
      <span class="brand-name">Skylark Aerial Tours</span>
    </div>

    <div class="contact">
      <div class="contact-lead">For bookings or more information:</div>
      <div class="contact-phone">call our friendly team on 1300 555 019</div>
      <div class="contact-line">emial us : flights@skylarkaerialtours.com.au</div>
      <div class="contact-line">log on : www.skylarkaerialtours.com.au</div>
      <div class="contact-social">Find us also on social media and travel review sites @skylarkaerialtours</div>
    </div>

    <div class="licence-band">Skylark Aerial Tours operates under Air Operator's Certificate C512870-03<br>issued by the National Air Safety Office</div>
  </div>
</div>
</body>
</html>
```